Managed Service Provider need new business cards

We are a small Maanged Service Provider of IT Services and need a new fresh design for our business cards. We want something impossible, fun and professional :)
Our services has a large range, but we are always fun and make sure our customers both get their issue sorted and also feel like they are "catching up with an old friend".
All our cards in the past has always been all black, with red and we need something fresher.
The back of card, we would like just a small list of what we do i think, but if someone has a better idea, please do something cool with the back of the card:
Managed IT Services
Productivity Solutions
Data Backup and Recovery
IT System Maintenance
Managed IT Security
More details can be found on our website tqnetworks.com.au
Industry/Entity Type
It Company
Contact Information for Business Card
Name: Dwayne Falstrup
Title: Director
Phone: 03 6193 4827
Mobile: 0412 587 239
Email: dwayne@tqnetworks.com.au
Web: www.tqnetworks.com.au

```html
<!DOCTYPE html>
<html lang="en">
<head>
<meta charset="utf-8">
<title>TQ Networks — Business Card</title>
<link href="https://fonts.googleapis.com/css2?family=Roboto:wght@400;500&family=Roboto+Condensed:wght@700&display=swap" rel="stylesheet">
<style>
  :root {
    --backdrop: #d9d9d9;
    --card-black: #0b0b0b;
    --card-black-soft: #1a1a1a;
    --brand-red: #e3161d;
    --text-white: #f2f2f2;
  }
  * { margin: 0; padding: 0; box-sizing: border-box; }
  html, body {
    width: 1200px;
    height: 800px;
    overflow: hidden;
    background: var(--backdrop);
  }
  .stage { position: relative; width: 1200px; height: 800px; }

  .card {
    position: absolute;
    top: 284px;
    width: 428px;
    height: 237px;
    background: linear-gradient(100deg, var(--card-black) 0%, var(--card-black-soft) 55%, var(--card-black) 100%);
    overflow: hidden;
  }
  .card--front { left: 112px; }
  .card--back { left: 638px; }

  /* Front */
  .holder { position: absolute; left: 28px; top: 22px; }
  .holder__name {
    font-family: "Roboto Condensed", sans-serif;
    font-weight: 700;
    font-size: 12.5px;
    color: var(--brand-red);
    text-transform: uppercase;
    letter-spacing: 0.1px;
    line-height: 15px;
  }
  .holder__title {
    font-family: "Roboto Condensed", sans-serif;
    font-weight: 700;
    font-size: 10px;
    color: var(--brand-red);
    text-transform: uppercase;
    line-height: 13px;
  }
  .contacts { position: absolute; left: 28px; top: 59px; list-style: none; }
  .contacts__item {
    display: flex;
    align-items: center;
    height: 13.3px;
    font-family: "Roboto", sans-serif;
    font-size: 10px;
    color: var(--text-white);
  }
  .contacts__icon { width: 8px; height: 8px; margin-right: 5px; fill: var(--brand-red); }

  .front-art {
    position: absolute;
    left: 106px;
    top: 56px;
    width: 316px;
    height: 180px;
    background: radial-gradient(ellipse at 60% 65%, rgba(227, 22, 29, 0.28) 0%, rgba(227, 22, 29, 0.08) 50%, rgba(227, 22, 29, 0) 75%);
  }

  /* Back */
  .brand-name {
    position: absolute;
    left: 46px;
    top: 96px;
    font-family: "Roboto Condensed", sans-serif;
    font-weight: 700;
    font-size: 22px;
    color: var(--brand-red);
    text-transform: uppercase;
    letter-spacing: 0.3px;
  }
  .services { position: absolute; left: 242px; top: 70px; list-style: none; }
  .services__item {
    display: flex;
    align-items: center;
    height: 19.8px;
    font-family: "Roboto", sans-serif;
    font-size: 10px;
    color: var(--text-white);
  }
  .services__marker {
    width: 5px;
    height: 5px;
    border-radius: 50%;
    background: var(--brand-red);
    margin-right: 23px;
  }
</style>
</head>
<body>
<main class="stage">

  <section class="card card--front" aria-label="Business card front">
    <div class="holder">
      <p class="holder__name">Dwayne Falstrup</p>
      <p class="holder__title">Director</p>
    </div>
    <ul class="contacts">
      <li class="contacts__item">
        <svg class="contacts__icon" viewBox="0 0 10 10" aria-hidden="true"><path d="M2 0.5 L3.6 2.6 L2.7 3.6 Q3.8 5.9 6.2 7.2 L7.3 6.3 L9.5 7.9 L8.4 9.5 Q3.5 9 0.5 1.7 Z"/></svg>
        03 6193 4827
      </li>
      <li class="contacts__item">
        <svg class="contacts__icon" viewBox="0 0 10 10" aria-hidden="true"><path d="M2.5 0 H7.5 V10 H2.5 Z M3.4 1 V8 H6.6 V1 Z"/></svg>
        0412 587 239
      </li>
      <li class="contacts__item">
        <svg class="contacts__icon" viewBox="0 0 10 10" aria-hidden="true"><path d="M0 1.5 H10 V8.5 H0 Z M0.8 2.2 L5 5.3 L9.2 2.2 Z" fill-rule="evenodd"/></svg>
        dwayne@tqnetworks.com.au
      </li>
      <li class="contacts__item">
        <svg class="contacts__icon" viewBox="0 0 10 10" aria-hidden="true"><circle cx="5" cy="5" r="4.5"/><path d="M0.5 5 H9.5 M5 0.5 V9.5" stroke="#0b0b0b" stroke-width="0.8"/></svg>
        www.tqnetworks.com.au
      </li>
    </ul>
    <div class="front-art" role="img" aria-label="Large red line illustration of a computer mouse with a sweeping cable"></div>
  </section>

  <section class="card card--back" aria-label="Business card back">
    <p class="brand-name">TQ Networks</p>
    <ul class="services">
      <li class="services__item"><span class="services__marker"></span>Managed IT Services</li>
      <li class="services__item"><span class="services__marker"></span>Productivity Solutions</li>
      <li class="services__item"><span class="services__marker"></span>Data Backup and Recovery</li>
      <li class="services__item"><span class="services__marker"></span>IT System Maintenance</li>
      <li class="services__item"><span class="services__marker"></span>Managed IT Security</li>
    </ul>
  </section>

</main>
</body>
</html>
```